Urgent - brand new business card for a startup technical advisory and incubation business in Sydney

We need a brand new business card design for BrightForge. We are a startup technical advisory and incubation business based in Sydney Australia. We work with entrepreneurs and innovators to help rapidly and efficiently turn their ideas into reality and to ensure they have the technical platform required for growth.

Our name is partly inspired by our love of lean product development methods and the lean startup movement.

We would like clean, uncluttered designs that feature our two logo colours and communicate a professional but creative, in-touch and entrepreneurial business.

PLEASE SEE MUST HAVE PRIORITIES FOR DRAFT CONTACT INFORMATION AND OTHER DESIRED TEXT ON CARD.
Updates

We have now updated the brief to include draft business card contact information and also some additional desired text to feature on the card design.    Please review the Must Have priorities.

Also final updated source files for the horizontal and vertical versions have now been uploaded and should be used for any designs.

Thanks!

Target Market(s)

Entrepeneurs, innovators, startup investors looking for a strong product development partner

Industry/Entity Type

Business

Requirements
Must have
• Feature our two logo colours
Be a relatively clean, pared back overall design - quite minimalist

Updated source files (AI) for vertical and horizontal layouts attached.

Draft contact information for business card:
Neil Barton
Founder & CTO
Phone: +61 427 555123
Email: xxxx@brightforge.com
Skype: xxxxxbarton
Twitter: nbarton

www.brightforge.com

We would also like the overall design to include the phrase "You have great ideas. Let us make them happen." (probably in a reasonably subtle way)

Nice to have
• Inspire me! Double-sided designs are fine with logo, phrase, (URL?) on one side and contact details on other (+ any other design elements)

Logo on business card can be either with lightbulb above the wording as per example here or to the left of the BrightForge wording - both layouts in files provided.
Should not have
• Shouldn't look like a Pentara Suite business card template :-)

```html
<!DOCTYPE html>
<html lang="en">
<head>
<meta charset="utf-8">
<title>BrightForge Business Card</title>
<link rel="stylesheet" href="https://fonts.googleapis.com/css2?family=Michroma&display=swap">
<style>
  :root {
    --page-bg: #ffffff;
    --card-black: #000000;
    --gloss: #2b2b2b;
    --panel-white: #ffffff;
    --brand-blue: #0a90da;
    --brand-blue-light: #7cc6f0;
    --label-ink: #0b0b0b;
    --contact-ink: #f2f2f2;
  }
  html, body {
    margin: 0;
    padding: 0;
    width: 1200px;
    height: 1000px;
    overflow: hidden;
    background: var(--page-bg);
  }
  .canvas {
    position: relative;
    width: 1200px;
    height: 1000px;
  }
  .card {
    position: absolute;
    left: 95px;
    top: 211px;
    width: 1010px;
    height: 578px;
    border-radius: 36px;
    background: var(--card-black);
    overflow: hidden;
  }
  .card-gloss {
    position: absolute;
    inset: 0;
    width: 100%;
    height: 100%;
  }
  .brand-panel {
    position: absolute;
    left: 0;
    top: 124px;
    width: 398px;
    height: 330px;
    background: var(--panel-white);
    border-radius: 0 46px 46px 0;
  }
  .brand-mark {
    position: absolute;
    left: 139px;
    top: 58px;
    width: 120px;
    height: 120px;
    border-radius: 50%;
    background: var(--brand-blue);
  }
  .brand-name {
    position: absolute;
    left: 0;
    width: 398px;
    top: 222px;
    text-align: center;
    font-family: "Michroma", sans-serif;
    font-size: 34px;
    color: var(--brand-blue);
    letter-spacing: 0.5px;
    margin: 0;
  }
  .contact-list {
    position: absolute;
    left: 414px;
    top: 192px;
    margin: 0;
    padding: 0;
    list-style: none;
  }
  .contact-row {
    display: flex;
    align-items: center;
    height: 50px;
    margin-bottom: 22px;
  }
  .contact-label {
    width: 228px;
    height: 50px;
    box-sizing: border-box;
    padding-left: 112px;
    display: flex;
    align-items: center;
    background:
      linear-gradient(200deg, var(--brand-blue-light) 0%, rgba(124,198,240,0) 35%),
      var(--brand-blue);
    border-top: 2px solid #3aa9e6;
    font-family: "Michroma", sans-serif;
    font-size: 21px;
    color: var(--label-ink);
  }
  .contact-value {
    margin-left: 36px;
    font-family: "Michroma", sans-serif;
    font-size: 17px;
    letter-spacing: 2px;
    font-variant: small-caps;
    color: var(--contact-ink);
    white-space: nowrap;
  }
</style>
</head>
<body>
<div class="canvas">
  <section class="card" aria-label="BrightForge business card">
    <svg class="card-gloss" viewBox="0 0 1010 578" aria-hidden="true">
      <defs>
        <linearGradient id="gloss-fade" x1="1" y1="0" x2="0.3" y2="1">
          <stop offset="0" stop-color="var(--gloss)"/>
          <stop offset="0.55" stop-color="#151515"/>
          <stop offset="1" stop-color="#000000"/>
        </linearGradient>
      </defs>
      <polygon points="750,0 1010,0 1010,578 555,578" fill="url(#gloss-fade)"/>
    </svg>

    <div class="brand-panel">
      <span class="brand-mark" aria-hidden="true"></span>
      <p class="brand-name">BrightForge</p>
    </div>

    <ul class="contact-list">
      <li class="contact-row">
        <span class="contact-label">Tel</span>
        <span class="contact-value">(020) 555-017-342</span>
      </li>
      <li class="contact-row">
        <span class="contact-label">Web</span>
        <span class="contact-value">www.BrightForge.com</span>
      </li>
      <li class="contact-row">
        <span class="contact-label">Email</span>
        <span class="contact-value">BrightForge@mailbox.net</span>
      </li>
    </ul>
  </section>
</div>
</body>
</html>
```